Tessa Kolbe Consulting

I am starting my own business and want to have a business card that stands out from the rest. Class is the word i use to describe what i would like to my card to look like.

I see my card as vibrant red card with rounded edges. mat finish
Centered scripted writing
large scripted font: Tessa Kolbe, smaller font & not scripted: Consulting, next line 0438715262, next line tessa@kolbehouse.com.au

i have now left 2 email message for the design of my card. Family is spelt wrong on the card. this needs to be correct and finial proof sent though!!! before i can download and approve
Tessa

Target Market(s)

Real Estate Professionals

Industry/Entity Type

Business

Contact Information for Business Card

Tessa Kolbe
Consulting
0438 715 262
tessa@kolbehouse.com.au

Logo Text

no logo

Requirements
Must have
• must have rounded edges

```html
<!DOCTYPE html>
<html lang="en">
<head>
<meta charset="utf-8">
<title>Tessa Kolbe Consulting – Business Card</title>
<link rel="stylesheet" href="https://fonts.googleapis.com/css2?family=Playball&family=Arvo&family=Questrial&display=swap">
<style>
  :root {
    --backdrop: #2b2b2b;
    --card-red-top: #952a32;
    --card-red-bottom: #b8262e;
    --ink: #ffffff;
    --rule: rgba(255, 255, 255, 0.55);
  }
  html, body {
    margin: 0;
    width: 1200px;
    height: 900px;
    overflow: hidden;
    background: var(--backdrop);
  }
  .business-card {
    position: absolute;
    left: 160px;
    top: 185px;
    width: 880px;
    height: 530px;
    border-radius: 42px;
    background: linear-gradient(170deg, var(--card-red-top) 0%, var(--card-red-bottom) 100%);
    color: var(--ink);
    overflow: hidden;
  }
  .corner-frame {
    position: absolute;
    inset: 0;
  }
  .corner-frame line {
    stroke: var(--rule);
    stroke-width: 1.5;
  }
  .identity {
    position: absolute;
    left: 0;
    right: 0;
    top: 130px;
    text-align: center;
  }
  .identity-lockup {
    display: inline-block;
    margin: 0;
    font-weight: 400;
  }
  .identity-name {
    display: block;
    font-family: "Playball", cursive;
    font-size: 108px;
    line-height: 1;
    letter-spacing: 1px;
  }
  .identity-tagline {
    display: block;
    text-align: right;
    margin-top: -2px;
    padding-right: 4px;
    font-family: "Arvo", serif;
    font-size: 28px;
    line-height: 1;
    letter-spacing: 0.5px;
  }
  .contact {
    position: absolute;
    left: 0;
    right: 0;
    top: 318px;
    margin: 0;
    text-align: center;
    font-style: normal;
  }
  .contact-phone {
    display: block;
    font-family: "Questrial", sans-serif;
    font-size: 32px;
    letter-spacing: 2px;
    line-height: 1.3;
  }
  .contact-email {
    display: block;
    font-family: "Arvo", serif;
    font-size: 26px;
    letter-spacing: 0.5px;
    line-height: 1.5;
  }
</style>
</head>
<body>
  <main class="business-card">
    <svg class="corner-frame" width="880" height="530" viewBox="0 0 880 530" aria-hidden="true">
      <line x1="40" y1="45" x2="250" y2="45"/>
      <line x1="40" y1="45" x2="40" y2="245"/>
      <line x1="630" y1="45" x2="840" y2="45"/>
      <line x1="840" y1="45" x2="840" y2="200"/>
      <line x1="40" y1="485" x2="250" y2="485"/>
      <line x1="40" y1="485" x2="40" y2="330"/>
      <line x1="630" y1="485" x2="840" y2="485"/>
      <line x1="840" y1="485" x2="840" y2="300"/>
    </svg>
    <header class="identity">
      <h1 class="identity-lockup">
        <span class="identity-name">Tessa Kolbe</span>
        <span class="identity-tagline">consulting</span>
      </h1>
    </header>
    <address class="contact">
      <span class="contact-phone">0438715262</span>
      <span class="contact-email">tessa@kolbehouse.com.au</span>
    </address>
  </main>
</body>
</html>
```